Bracken Project Services - Flyer

I need a single page A4 Capability Statement, which will be used to market our services to prospective clients, both in print and via email PDF.
It needs to look professional and should incorporate the elements I have uploaded into files, these include:
Capability Statement Text
Bracken Services Company Logo
Additional Logo’s (Tools We Use)
Frame Cellar Pics can be cut into the page
I have included examples of capability statements as a guide to what i am looking for.
Regards
Derek
Engineering Consulting

```html
<!DOCTYPE html>
<html lang="en">
<head>
<meta charset="utf-8">
<title>Bracken Project Services – Capability Statement</title>
<link rel="stylesheet" href="https://fonts.googleapis.com/css2?family=Open+Sans:ital,wght@0,300;0,400;0,700;1,700&family=PT+Sans:wght@400;700&display=swap">
<style>
  :root {
    --backdrop: #8c8c8c;
    --paper: #ffffff;
    --brand-blue: #0d72bc;
    --box-blue: #0f75bd;
    --ink: #3c3c3c;
    --ink-soft: #555555;
    --rule: #9a9a9a;
  }
  * { margin: 0; padding: 0; box-sizing: border-box; }
  html, body { width: 1200px; height: 1200px; overflow: hidden; }
  body { background: var(--backdrop); font-family: "Open Sans", sans-serif; color: var(--ink); }

  .flyer {
    position: absolute; left: 190px; top: 20px;
    width: 820px; height: 1160px; background: var(--paper);
  }

  .hero-photo {
    position: absolute; left: 0; top: 0; width: 820px; height: 296px;
    background: linear-gradient(120deg, #dfe9f3 0%, #f4f7fb 35%, #e4eef6 60%, #c9dbe9 100%);
  }

  .brand-block { position: absolute; left: 42px; top: 345px; width: 314px; text-align: center; }
  .brand-mark {
    display: block; width: 74px; height: 74px; margin: 0 auto 16px;
    border-radius: 50%; background: var(--brand-blue);
  }
  .brand-name {
    font-family: "PT Sans", sans-serif; font-weight: 700; font-size: 19px;
    letter-spacing: 1px; color: var(--brand-blue); line-height: 1.15;
  }
  .contact { margin-top: 32px; font-size: 12.4px; font-weight: 300; line-height: 20.6px; color: var(--ink-soft); }

  .divider-vertical {
    position: absolute; left: 354px; top: 331px; width: 3px; height: 288px; background: var(--brand-blue);
  }

  .headline { position: absolute; left: 387px; top: 318px; width: 420px; }
  .headline h1 {
    font-family: "PT Sans", sans-serif; font-weight: 700; font-size: 51px;
    line-height: 61px; color: var(--brand-blue); letter-spacing: -0.3px;
  }
  .headline .tagline {
    margin-top: 3px; font-size: 33px; font-weight: 300; line-height: 44.5px; color: var(--ink-soft);
  }
  .headline .tagline strong { font-family: "PT Sans", sans-serif; font-weight: 700; font-size: 36px; color: #444; }

  .services {
    position: absolute; left: 42px; top: 649px; width: 314px; height: 429px;
    background: var(--box-blue); color: #fff; text-align: center; padding-top: 15px;
    font-size: 12.6px; font-weight: 300; line-height: 16.5px;
  }
  .services h2 {
    font-size: 15.5px; font-weight: 700; text-decoration: underline; line-height: 20px;
  }
  .services h3 { font-size: 12.8px; font-weight: 700; font-style: italic; margin: 3px 0 2px; }
  .services ul { list-style: none; }
  .services .group + .group { margin-top: 16px; }
  .services .group.cost { margin-top: 12px; }

  .about { position: absolute; left: 387px; top: 648px; width: 386px; }
  .about p {
    font-size: 12.3px; font-weight: 300; line-height: 17px; color: var(--ink-soft);
    text-align: justify; margin-bottom: 16px;
  }

  .schedule-photo {
    position: absolute; left: 387px; top: 848px; width: 386px; height: 230px;
    background: linear-gradient(160deg, #eef3f8 0%, #dde6ef 55%, #c7d3df 100%);
  }

  .tool-strip {
    position: absolute; left: 42px; top: 1106px; width: 731px; height: 28px;
    display: flex; align-items: center; justify-content: space-between;
  }
  .tool {
    font-family: "Open Sans", sans-serif; font-weight: 700; font-size: 11px; color: #555;
    display: flex; align-items: center; gap: 5px; white-space: nowrap;
  }
  .tool .dot { width: 9px; height: 9px; background: var(--brand-blue); display: inline-block; }
  .tool-sep { width: 1px; height: 26px; background: var(--rule); }
</style>
</head>
<body>
  <main class="flyer">
    <div class="hero-photo" role="img" aria-label="Photo of colleagues reviewing printed charts and reports at a desk"></div>

    <section class="brand-block">
      <span class="brand-mark" aria-hidden="true"></span>
      <div class="brand-name">BRACKEN PROJECT<br>SERVICES</div>
      <div class="contact">
        Derek Halloran (Managing Director)<br>
        info@brackenservices.ie<br>
        www.brackenservices.ie<br>
        +353 (0)871550192
      </div>
    </section>

    <div class="divider-vertical"></div>

    <section class="headline">
      <h1>BRACKEN PROJECT<br>SERVICES LTD.</h1>
      <p class="tagline">is a leading<br>project control<br>consultancy based<br>in <strong>Co Cork Ireland</strong></p>
    </section>

    <section class="services">
      <div class="group">
        <h2>CORE SERVICES</h2>
        <h3>Planning and Scheduling</h3>
        <ul>
          <li>Tender Planning</li>
          <li>Interactive Planning / Pull Planning</li>
          <li>EPCMV Planning &amp; Scheduling</li>
          <li>Schedule Earned Value Management</li>
          <li>Independent Schedule Quality Assessment</li>
          <li>Schedule Risk Analysis (Monte Carlo)</li>
          <li>Training</li>
        </ul>
      </div>
      <div class="group">
        <h3>Management of Risk</h3>
        <ul>
          <li>Risk Management Policies &amp; Procedures</li>
          <li>Risk Management Strategy</li>
          <li>Risk Registers</li>
          <li>Risk Improvement Planning</li>
          <li>Risk Response and Communication</li>
          <li>Risk Management Training</li>
        </ul>
      </div>
      <div class="group cost">
        <h2>COST CONTROL</h2>
        <ul>
          <li>Estimating &amp; Forecasting</li>
          <li>Earned Value Analysis</li>
          <li>Progress Reporting</li>
          <li>Cost Risk Analysis</li>
        </ul>
      </div>
    </section>

    <section class="about">
      <p>For over 20 years we have been helping our clients to deliver complex projects and programs throughout mainland Europe.</p>
      <p>We are passionate about empower organisations to achieve their objectives, on time and on budget.</p>
      <p>We are continually innovating, evolving and learning, utilize the latest industry tools and techniques to deliver real value to our clients.</p>
      <p>Our goal is to make successful project delivery more achievable and repeatable.</p>
    </section>

    <div class="schedule-photo" role="img" aria-label="Photo of a printed Gantt schedule with a pen"></div>

    <footer class="tool-strip">
      <span class="tool">Northwall Planner</span>
      <span class="tool-sep"></span>
      <span class="tool"><span class="dot"></span>Taskgrid</span>
      <span class="tool-sep"></span>
      <span class="tool">Waypoint Pro</span>
      <span class="tool-sep"></span>
      <span class="tool"><span class="dot"></span>Stratum Schedule</span>
      <span class="tool-sep"></span>
      <span class="tool">Keelson Gauge</span>
      <span class="tool-sep"></span>
      <span class="tool">RiskFrame</span>
    </footer>
  </main>
</body>
</html>
```